The place is called Fern-O-Lune Hall. It's in the county between the cities of Dunmere & Kestrelton, hence the name of the area. It had been a bar w/food for 50 years but was closed for 5yrs. It's all cleaned up, remodeled & raring to go. The bar opened in February and has had live music with no cover charge every week-end. Now the kitchen side (Called NoNa J's PIZZA & PASTA) opened Nov 1st. We have already owned the family restaurant right next door - called Pop T's Family Restaurant for 16 years. Pop T's is wildly successful, but sells no Italian food whatsoever, so the NoNa J's of us is opening right next door as competition. However, only 1 pizza competitor is in our area of about 3500 people. We would like for you to design 3 postcards as coupons. We are going to send a first mailing to about 400 homes. The 2nd card they rec. will depend on whether or not they used the first one. Get it? I have made over 20 TV commercials, if you would like to watch a sample of my advertising humor, go to our website, popts-familydiner.example. The drift is this is a NEW Pizza place called NoNa J's located inside Fern-O-Lune Hall. Folks in this small neck of the woods will get the drift that the two places are related, and we're trying to draw off the goodwill of the name Pop T's. So far as the first postcard should offer a $5.00 coupon for Pop T's for buying ANY pizza at NoNa J's.

```html
<!DOCTYPE html>
<html lang="en">
<head>
<meta charset="utf-8">
<title>NoNa J's Pizza &amp; Pasta — Postcard</title>
<link rel="stylesheet" href="https://fonts.googleapis.com/css2?family=Roboto+Condensed:ital,wght@0,400;0,700;1,700&family=Roboto+Slab:wght@700&family=Libre+Baskerville:wght@700&display=swap">
<style>
  :root {
    --backdrop: #5a4030;
    --gold-light: #fbe3a0;
    --gold: #f4c15a;
    --gold-deep: #e9a83c;
    --red: #a3182b;
    --red-bright: #d4202f;
    --green: #1f7a3a;
    --green-bright: #23a04a;
    --ink: #222;
    --cream: #fdf2d6;
    --white: #fff;
  }
  * { box-sizing: border-box; margin: 0; padding: 0; }
  html, body { width: 1200px; height: 500px; overflow: hidden; }
  body {
    background: var(--backdrop);
    font-family: "Roboto Condensed", "Arial Narrow", sans-serif;
    position: relative;
  }
  .card {
    position: absolute; top: 35px; width: 556px; height: 435px; overflow: hidden;
  }
  /* FRONT */
  .card--front {
    left: 32px;
    background: radial-gradient(ellipse at 50% 35%, var(--gold-light) 0%, var(--gold) 60%, var(--gold-deep) 100%);
  }
  .brand-name {
    position: absolute; left: 42px; top: 20px;
    font-weight: 700; font-size: 56px; color: var(--red); line-height: 1;
  }
  .brand-sub {
    position: absolute; left: 62px; top: 90px;
    font-family: "Libre Baskerville", serif; font-weight: 700; font-size: 26px; color: var(--green);
  }
  .ribbon {
    position: absolute; left: 40px; top: 122px; width: 290px; height: 30px;
  }
  .ribbon svg { position: absolute; inset: 0; }
  .ribbon-text {
    position: relative; text-align: center; line-height: 30px;
    font-weight: 700; font-size: 17px; color: var(--red);
  }
  .new-place {
    position: absolute; left: 370px; top: 14px;
    font-weight: 700; font-style: italic; font-size: 20px; color: var(--red-bright);
  }
  .venue-badge { position: absolute; left: 388px; top: 43px; width: 92px; }
  .venue-badge__label {
    background: var(--red-bright); color: var(--white); text-align: center;
    font-weight: 700; font-size: 12px; line-height: 14px; padding: 3px 2px;
  }
  .venue-badge__name {
    background: #111; color: var(--white); height: 72px;
    display: flex; align-items: center; justify-content: center; text-align: center;
    font-weight: 700; font-size: 15px; line-height: 1.1; padding: 4px;
  }
  .pizza-photo {
    position: absolute; left: 0; top: 150px; width: 556px; height: 240px;
    background: radial-gradient(ellipse at 40% 50%, #f1d28a 0%, #e0a24a 45%, #b5492c 75%, rgba(180,80,40,0) 100%);
  }
  .coupon {
    position: absolute; left: 256px; top: 233px; width: 286px; height: 140px;
    background: var(--white); border: 3px dashed var(--ink); border-radius: 14px;
    text-align: center; padding: 10px 8px 0 40px;
  }
  .coupon__line1 { font-weight: 700; font-size: 28px; color: var(--ink); line-height: 1.1; }
  .coupon__line1 b { font-family: "Roboto Slab", serif; color: var(--red); font-size: 30px; }
  .coupon__line2 { font-weight: 700; font-size: 24px; color: var(--ink); line-height: 1.2; }
  .coupon__line2 em { font-style: normal; color: var(--red-bright); }
  .coupon__brand { font-weight: 700; font-size: 34px; color: var(--green); line-height: 1.2; }
  .price-badge {
    position: absolute; left: 200px; top: 254px; width: 96px; height: 96px; border-radius: 50%;
    background: var(--red-bright); border: 6px solid var(--green); box-shadow: 0 0 0 3px var(--white) inset;
    color: var(--white); font-weight: 700; font-size: 58px; line-height: 84px; text-align: center;
  }
  .price-badge sup { font-size: 28px; vertical-align: 22px; }
  .contact-band {
    position: absolute; left: 0; bottom: 0; width: 100%; height: 45px;
    background: var(--green); color: var(--white);
    display: flex; align-items: center; justify-content: center; gap: 6px;
    font-size: 19px;
  }
  .icon-phone { width: 18px; height: 18px; }
  /* BACK */
  .card--back { left: 614px; background: var(--white); }
  .back-info {
    position: absolute; left: 0; top: 0; width: 279px; height: 320px;
    background: linear-gradient(90deg, var(--cream) 0%, #fbe6b4 100%);
    padding: 0 0 0 26px;
  }
  .about-tag { position: absolute; left: 24px; top: 22px; width: 216px; height: 24px; }
  .about-tag svg { position: absolute; inset: 0; }
  .about-tag span {
    position: relative; display: block; line-height: 24px; padding-left: 22px;
    font-weight: 700; font-size: 14px; color: var(--ink);
  }
  .about-headline {
    position: absolute; left: 26px; top: 50px; width: 250px;
    font-weight: 700; font-size: 20px; line-height: 1.08; color: var(--red);
  }
  .amenities { position: absolute; left: 26px; top: 102px; list-style: none; font-size: 13px; color: var(--ink); line-height: 20px; }
  .amenities li::before { content: "●"; color: var(--red); font-size: 9px; margin-right: 5px; vertical-align: 2px; }
  .tagline-green {
    position: absolute; left: 42px; top: 170px;
    font-weight: 700; font-size: 16px; color: var(--green);
  }
  .pasta-art {
    position: absolute; left: 30px; top: 198px; width: 44px; height: 44px; border-radius: 50%;
    background: radial-gradient(circle, #c54a8e 0%, #7a3a94 70%);
  }
  .hours {
    position: absolute; left: 72px; top: 206px;
    font-weight: 700; font-size: 15px; line-height: 20px; color: var(--red);
  }
  .pickup { position: absolute; left: 0; top: 260px; width: 279px; text-align: center; font-size: 13px; line-height: 17px; color: var(--ink); }
  .pickup strong { font-weight: 700; }
  .return-address { position: absolute; left: 356px; top: 18px; text-align: center; color: var(--ink); font-size: 12px; line-height: 15px; }
  .return-address__name { font-weight: 700; font-size: 24px; color: var(--red); line-height: 1.1; }
  .return-address__sub { font-family: "Libre Baskerville", serif; font-weight: 700; font-size: 11px; color: var(--green); margin-bottom: 5px; }
  .stamp-box { position: absolute; right: 8px; top: 20px; width: 54px; height: 62px; border: 3px dashed #bbb; }
  .back-band {
    position: absolute; left: 0; top: 320px; width: 100%; height: 36px;
    background: var(--green-bright); color: var(--white);
    display: flex; align-items: center; padding-left: 184px; gap: 6px;
    font-weight: 700; font-size: 22px; letter-spacing: 1px;
  }
</style>
</head>
<body>
  <section class="card card--front" aria-label="Postcard front">
    <div class="pizza-photo" role="img" aria-label="Photo of a pepperoni, mushroom and olive pizza with a slice being pulled away"></div>
    <div class="brand-name">NoNa J's</div>
    <div class="brand-sub">PIZZA &amp; PASTA</div>
    <div class="ribbon">
      <svg viewBox="0 0 290 30" preserveAspectRatio="none"><polygon points="0,0 290,0 278,15 290,30 0,30 12,15" fill="#f6c24d"/></svg>
      <div class="ribbon-text">PPP ★ Pizza, Pasta &amp; Pub ★</div>
    </div>
    <div class="new-place">New Pizza Place!</div>
    <div class="venue-badge">
      <div class="venue-badge__label">LOCATED<br>INSIDE</div>
      <div class="venue-badge__name">Fern-O-Lune Hall</div>
    </div>
    <div class="coupon">
      <div class="coupon__line1">For <b>Pop T's</b></div>
      <div class="coupon__line2">If you buy <em>ANY</em> Pizza at</div>
      <div class="coupon__brand">NoNa J's</div>
    </div>
    <div class="price-badge"><sup>$</sup>5</div>
    <div class="contact-band">
      <svg class="icon-phone" viewBox="0 0 24 24"><circle cx="12" cy="12" r="11" fill="none" stroke="#fff" stroke-width="2"/><path d="M8 6c1 0 2 2 2 3s-1 1-1 2 2 4 3 4 1-1 2-1 3 1 3 2-1 2-2 2C10 18 6 12 6 8c0-1 1-2 2-2z" fill="#fff"/></svg>
      <span>555.014.2290 | 1820 W. Alder Street, Dunmere, IL&nbsp; 61199</span>
    </div>
  </section>

  <section class="card card--back" aria-label="Postcard back">
    <div class="back-info">
      <div class="about-tag">
        <svg viewBox="0 0 216 24" preserveAspectRatio="none">
          <polygon points="0,0 14,0 14,24 0,24 6,12" fill="#1f7a3a"/>
          <rect x="14" y="0" width="188" height="24" fill="#fff"/>
          <polygon points="202,0 216,0 210,12 216,24 202,24" fill="#a3182b"/>
        </svg>
        <span>About NoNa J's Pizza &amp; Pasta</span>
      </div>
      <h2 class="about-headline">A new Pizza place located inside Fern-O-Lune Hall.</h2>
      <ul class="amenities">
        <li>Full bar with live shows on Saturdays</li>
        <li>Pool, Darts, and video gaming</li>
        <li>Daily drink specials</li>
      </ul>
      <div class="tagline-green">PPP ★ Pizza, Pasta &amp; Pub ★</div>
      <div class="pasta-art" role="img" aria-label="Illustration of pasta swirl and pizza"></div>
      <div class="hours">Pizza &amp; Pasta Served Daily<br>From 10:00 AM to 10:00 PM</div>
      <p class="pickup"><strong>Pick up our Homemade Pizza Today.</strong><br>Or Come In and Observe Us<br>While We Make It.</p>
    </div>
    <div class="return-address">
      <div class="return-address__name">NoNa J's</div>
      <div class="return-address__sub">PIZZA &amp; PASTA</div>
      1820 W. Alder St.<br>Dunmere, IL
    </div>
    <div class="stamp-box" aria-label="Stamp area"></div>
    <div class="back-band">
      <svg class="icon-phone" viewBox="0 0 24 24"><circle cx="12" cy="12" r="11" fill="none" stroke="#fff" stroke-width="2"/><path d="M8 6c1 0 2 2 2 3s-1 1-1 2 2 4 3 4 1-1 2-1 3 1 3 2-1 2-2 2C10 18 6 12 6 8c0-1 1-2 2-2z" fill="#fff"/></svg>
      <span>555.014.2290</span>
    </div>
  </section>
</body>
</html>
```